Amber Reed Wellness Buisness Cards

I am looking to create a business card for a healing business. In the business I provide coaching and Reiki. I am a licensed LCPC (licensed clinical professional counselor)

Amber Reed Wellness
Soul Centered Healing, Reiki Healinig

Lena Dovrahi, L.C.P.C

The card should include the following
biz name: Amber Reed Wellness
my name: Lena Dovrahi
website: Lenadovrahi.example
email: lena.pastum@mailbox.example
instagram handle: lenapastumdovrahi

Target Market(s)

Women ages 25-65

```html
<!DOCTYPE html>
<html lang="en">
<head>
<meta charset="utf-8">
<title>Amber Reed Wellness – Business Card</title>
<link rel="stylesheet" href="https://fonts.googleapis.com/css2?family=Open+Sans:wght@400;600;700&display=swap">
<style>
  :root {
    --teal-blue: #2e7c9f;
    --mint: #3ecf95;
    --white: #ffffff;
    --ink-blue: #2b6f8f;
    --text-dark: #3a3f44;
    --backdrop: #eceff1;
  }
  * { box-sizing: border-box; margin: 0; padding: 0; }
  html, body {
    width: 1200px; height: 900px; overflow: hidden;
    background: var(--backdrop);
    font-family: "Open Sans", Arial, sans-serif;
  }
  .canvas { position: relative; width: 1200px; height: 900px; }

  .card {
    position: absolute;
    width: 560px; height: 320px;
    border-radius: 4px;
    overflow: hidden;
    box-shadow: 0 10px 28px rgba(0,0,0,0.18);
  }

  /* Front side */
  .card--front {
    left: 70px; top: 120px;
    background: var(--teal-blue);
    color: var(--white);
    text-align: center;
  }
  .card--front .brand-name {
    position: absolute; left: 0; right: 0; top: 96px;
    font-weight: 700; font-size: 38px; letter-spacing: 1px;
    text-transform: uppercase;
  }
  .card--front .divider {
    position: absolute; left: 150px; width: 260px; top: 172px;
    height: 2px; background: var(--mint);
  }
  .card--front .taglines {
    position: absolute; left: 0; right: 0; top: 196px;
    font-size: 13.5px; line-height: 1.45; letter-spacing: 0.6px;
    text-transform: uppercase;
  }

  /* Back side */
  .card--back {
    left: 570px; top: 470px;
    background: var(--white);
  }
  .card--back .wave { position: absolute; inset: 0; }
  .holder-name {
    position: absolute; left: 44px; top: 48px;
    font-weight: 700; font-size: 21px; letter-spacing: 0.5px;
    text-transform: uppercase; color: var(--ink-blue);
  }
  .holder-name .surname { color: var(--mint); }
  .brand-lockup {
    position: absolute; right: 34px; top: 52px;
    display: flex; flex-direction: column; align-items: flex-end;
  }
  .brand-lockup .brand-row { display: flex; align-items: center; gap: 7px; }
  .brand-lockup .mark {
    width: 11px; height: 11px; border-radius: 50%; background: var(--mint);
  }
  .brand-lockup .brand-name {
    font-weight: 700; font-size: 19px; color: var(--ink-blue);
    text-transform: uppercase; letter-spacing: 0.5px;
  }
  .brand-lockup .divider {
    margin-top: 10px; width: 150px; height: 2px; background: var(--mint);
  }
  .contacts {
    position: absolute; left: 44px; top: 148px;
    list-style: none; font-size: 13px; color: var(--text-dark);
  }
  .contacts li { display: flex; align-items: center; gap: 7px; height: 20px; }
  .contacts svg { width: 12px; height: 12px; flex: none; }
</style>
</head>
<body>
<main class="canvas">

  <section class="card card--front">
    <div class="brand-name">Amber Reed Wellness</div>
    <div class="divider"></div>
    <p class="taglines">Soul Centered Coaching | Reiki Healing<br>Certified Crystal Reiki Master</p>
  </section>

  <section class="card card--back">
    <svg class="wave" viewBox="0 0 560 320" preserveAspectRatio="none" aria-hidden="true">
      <path d="M0 270 C220 268 310 250 390 185 C450 134 510 114 560 110 L560 320 L0 320 Z" fill="var(--mint)"/>
      <path d="M0 284 C220 282 315 260 395 194 C455 142 512 121 560 117 L560 320 L0 320 Z" fill="var(--white)"/>
      <path d="M0 294 C220 292 322 268 400 202 C460 150 515 128 560 124 L560 320 L0 320 Z" fill="var(--teal-blue)"/>
    </svg>

    <div class="holder-name">Lena <span class="surname">Dovrahi</span></div>

    <div class="brand-lockup">
      <div class="brand-row">
        <span class="mark"></span>
        <span class="brand-name">Amber Reed Wellness</span>
      </div>
      <div class="divider"></div>
    </div>

    <ul class="contacts">
      <li>
        <svg viewBox="0 0 13 13" aria-hidden="true"><rect width="13" height="13" rx="2" fill="var(--ink-blue)"/></svg>
        lenapastumdovrahi
      </li>
      <li>
        <svg viewBox="0 0 13 13" aria-hidden="true">
          <circle cx="6.5" cy="6.5" r="6" fill="var(--ink-blue)"/>
          <ellipse cx="6.5" cy="6.5" rx="2.6" ry="6" fill="none" stroke="var(--white)" stroke-width="0.9"/>
          <line x1="0.5" y1="6.5" x2="12.5" y2="6.5" stroke="var(--white)" stroke-width="0.9"/>
        </svg>
        www.Lenadovrahi.example
      </li>
      <li>
        <svg viewBox="0 0 13 13" aria-hidden="true">
          <rect x="0" y="2" width="13" height="9" fill="var(--ink-blue)"/>
          <polyline points="0.5,2.5 6.5,7.5 12.5,2.5" fill="none" stroke="var(--white)" stroke-width="1"/>
        </svg>
        lena.pastum@mailbox.example
      </li>
    </ul>
  </section>

</main>
</body>
</html>
```